Mortgage Protection Insurance Flyer

The target audience are new home owners so the design needs to be clean and simple.

This a primarily for Final Expense Insurance, but need an area where it says "We Also Specialize In:"
- Medicare Supplement Insurance (MediGap)
- Annuities
- Final Expense

All flyer versions need to be editable. Colors to be used are red, white or black. Refer to my website for colors and photos (harborvaleassurance.com). Will attach my logo and a flyer that I found online that is the format that I am looking for (for 8.5 in. x 11 in version). Need flyer in standard letter size 8.5 in. x11 in. but also in 8.5 in. x 5.5 in and 5.0 in. x 8.0 in. All sizes to be portrait oriented. If picked as winning design, need all flyer versions in full color, also in grey scale and files in all industry file types.

Content can be taken from my website..... harborvaleassurance.com

Do NOT submit if you are not willing to provide all versions as described above for the original project price.

Must use royalty-free stock photos please.

Target Market(s)

New homeowners looking for insurance to protect there mortgage payments

Industry/Entity Type

Life Insurance

Colors
f69fa3

Requirements
Must have
• Colors to be used are red, white or black.
• Need flyer in standard letter size 8.5 in. x11 in. but also in 3.5 in. x 8.5 in (Full Bleed 3.75 in by 8.75 in.) and 4.0 in. x 6.0 in. (Full Bleed 4.12 in x 6.12 in) Each design tailored to the size dimensions (So no squeezing 8.5 x 11 design into a 4.0 x 6.0 space.) All sizes to be portrait oriented. If picked as winning design, need all flyer versions in full color, also in grey scale and files in all file types.
• Do not need physical address on flyer, do need email address on flyer though - tkerlow@harborvaleassurance.com
• So phone number should be prominent, email address and website address should also be contact area.
• If you can not agree to terms above, do not submit any designs.
• Need facebook & twitter logos somewhere in contact info area.
Nice to have
• See sample flyers I have attached.
• White background with red used as primary graphic color and black used as secondary graphic if needed.
• font to be used should similar to one used in logo.

```html
<!DOCTYPE html>
<html lang="en">
<head>
<meta charset="utf-8">
<title>Harbor Vale Assurance – Flyer</title>
<link href="https://fonts.googleapis.com/css2?family=Montserrat:wght@700;800&family=Didact+Gothic&family=Open+Sans:wght@400&family=Kaushan+Script&display=swap" rel="stylesheet">
<style>
  :root{
    --red:#d10000;
    --red-deep:#b80000;
    --red-soft:#d99593;
    --ink:#1b1b1b;
    --white:#ffffff;
    --stage:#6e6e6e;
  }
  *{margin:0;padding:0;box-sizing:border-box}
  html,body{width:713px;height:1200px;overflow:hidden;background:var(--stage)}
  .flyer{position:absolute;left:16px;top:119px;width:680px;height:962px;background:var(--white);overflow:hidden;box-shadow:0 6px 18px rgba(0,0,0,.45)}
  .flyer-art{position:absolute;inset:0}
  .brand{position:absolute;left:34px;top:38px;font-family:"Montserrat",sans-serif;font-weight:800;color:var(--ink);line-height:1;letter-spacing:.5px}
  .brand-name{font-size:30px;display:block}
  .brand-sub{font-size:13px;display:block;margin-top:4px;letter-spacing:3px}
  .promise{position:absolute;left:373px;top:216px;width:224px;text-align:center;color:var(--white)}
  .promise-title{font-family:"Kaushan Script",cursive;font-size:30px;line-height:1.02}
  .promise-text{font-family:"Open Sans",sans-serif;font-size:11.5px;line-height:1.4;margin-top:12px}
  .section-title{position:absolute;left:33px;top:478px;font-family:"Montserrat",sans-serif;font-weight:800;font-size:41px;color:var(--red);letter-spacing:.2px;white-space:nowrap}
  .service{position:absolute}
  .service h3{font-family:"Montserrat",sans-serif;font-weight:700;font-size:17.5px;color:var(--ink);line-height:1.25;padding-left:26px;position:relative}
  .service h3 svg{position:absolute;left:0;top:5px;width:14px;height:14px}
  .service ul{list-style:none;margin-top:10px}
  .service li{font-family:"Didact Gothic",sans-serif;font-size:12.6px;line-height:1.15;color:var(--ink);position:relative;padding-left:22px;margin-bottom:8px}
  .service li::before{content:"";position:absolute;left:2px;top:4px;width:7px;height:7px;border-radius:50%;background:var(--red)}
  .service p{font-family:"Didact Gothic",sans-serif;font-size:12.6px;line-height:1.2;color:var(--ink);margin:8px 0 0 26px;text-align:justify}
  .final-expense{left:32px;top:555px;width:258px}
  .final-expense ul{margin-left:26px}
  .final-expense li{padding-left:21px}
  .mortgage{left:321px;top:555px;width:322px}
  .mortgage h3{white-space:nowrap}
  .mortgage li{text-align:justify}
  .medigap{left:32px;top:708px;width:268px}
  .medigap h3{font-size:19px}
  .contact{position:absolute;left:57px;top:866px;color:var(--white);font-family:"Didact Gothic",sans-serif}
  .contact-phone{font-size:25px;letter-spacing:.5px;line-height:1.1}
  .contact-line{font-size:10.5px;margin-top:4px;line-height:1.2}
  .contact-line:first-of-type{margin-top:7px}
  .contact-follow{font-size:11px;margin-top:6px;display:flex;align-items:center;gap:4px}
  .social-dot{width:14px;height:14px;border-radius:50%;background:var(--white);display:inline-block}
</style>
</head>
<body>
<main class="flyer">
  <svg class="flyer-art" width="680" height="962" viewBox="0 0 680 962">
    <defs>
      <linearGradient id="familyTone" x1="0" y1="0" x2="1" y2="1">
        <stop offset="0" stop-color="#c9b7a0"/>
        <stop offset=".45" stop-color="#a98463"/>
        <stop offset=".75" stop-color="#6f7f96"/>
        <stop offset="1" stop-color="#8fa3c2"/>
      </linearGradient>
      <linearGradient id="homeTone" x1="0" y1="0" x2="0" y2="1">
        <stop offset="0" stop-color="#9a6b58"/>
        <stop offset=".5" stop-color="#c8bfb8"/>
        <stop offset="1" stop-color="#5a6b86"/>
      </linearGradient>
      <clipPath id="homeClip"><circle cx="529" cy="892" r="184"/></clipPath>
    </defs>

    <path role="img" aria-label="Photo of a smiling three-generation family outdoors"
          fill="url(#familyTone)"
          d="M0,0 H680 V375 C630,330 590,330 520,370 C420,420 280,430 150,395 C80,375 30,350 0,325 Z"/>
    <path class="photo-swoosh" fill="var(--red)"
          d="M0,330 C70,395 170,432 270,432 C370,432 450,405 520,382 L525,396 C450,422 370,442 270,442 C160,442 70,405 0,352 Z"/>
    <path class="photo-swoosh-right" fill="var(--red)"
          d="M590,300 C630,318 662,340 680,362 V388 C660,362 625,340 590,330 Z"/>

    <circle class="badge-shadow" cx="476" cy="346" r="134" fill="var(--red-soft)"/>
    <circle class="badge" cx="485" cy="325" r="134" fill="var(--red-deep)"/>

    <g clip-path="url(#homeClip)">
      <rect role="img" aria-label="Photo of a young couple with a baby sitting on the steps of their new home"
            x="340" y="700" width="380" height="400" fill="url(#homeTone)"/>
    </g>
    <path class="home-ring" fill="none" stroke="var(--red)" stroke-width="2"
          d="M366,960 C340,880 360,780 440,740 C520,700 620,710 680,770"/>

    <path class="contact-band" fill="var(--red)"
          d="M0,849 C110,843 210,850 262,872 C300,890 316,925 324,962 H0 Z"/>
  </svg>

  <div class="brand">
    <span class="brand-name">HARBOR VALE</span>
    <span class="brand-sub">ASSURANCE</span>
  </div>

  <div class="promise">
    <div class="promise-title">Our Plans<br>Are Based On<br>Yours</div>
    <p class="promise-text">Get the right Final Expense Insurance, Medicare Supplement Insurance, Annuities or Mortgage Protection Insurance plan for your family's peace-of-mind!</p>
  </div>

  <h2 class="section-title">What We Specialize In</h2>

  <section class="service final-expense">
    <h3><svg viewBox="0 0 16 16"><path d="M13.5,8 A5.5,5.5 0 1 1 10.5,3.1" fill="none" stroke="var(--ink)" stroke-width="1.8"/><path d="M5,7.5 L8,10.5 L14,3.5" fill="none" stroke="var(--ink)" stroke-width="1.8"/></svg>Final Expense Insurance</h3>
    <ul>
      <li>Relatively low monthly premiums</li>
      <li>Premiums can never increase</li>
      <li>Your policy can never be cancelled as long as you pay your premium</li>
      <li>Many policies are Guaranteed Acceptance</li>
    </ul>
  </section>

  <section class="service mortgage">
    <h3><svg viewBox="0 0 16 16"><path d="M13.5,8 A5.5,5.5 0 1 1 10.5,3.1" fill="none" stroke="var(--ink)" stroke-width="1.8"/><path d="M5,7.5 L8,10.5 L14,3.5" fill="none" stroke="var(--ink)" stroke-width="1.8"/></svg>Mortgage Protection Insurance</h3>
    <ul>
      <li>Guaranteed approval. Even if you're in poor health or work in a dangerous profession, there is guaranteed approval with no medical exams or lab tests.</li>
      <li>Disability protection. Many MPI policies make mortgage payments (usually for a limited time) if you become disabled or lose your job.</li>
    </ul>
  </section>

  <section class="service medigap">
    <h3><svg viewBox="0 0 16 16"><path d="M13.5,8 A5.5,5.5 0 1 1 10.5,3.1" fill="none" stroke="var(--ink)" stroke-width="1.8"/><path d="M5,7.5 L8,10.5 L14,3.5" fill="none" stroke="var(--ink)" stroke-width="1.8"/></svg>Medicare Supplement Insurance (MediGap)</h3>
    <p>Medicare Supplement Insurance (also called MediGap) helps pay the “gap” between what Original Medicare (Medicare Parts A and B) pays and what you pay out of your own pocket.</p>
  </section>

  <footer class="contact">
    <div class="contact-phone">(208)555.0147</div>
    <div class="contact-line">tkerlow@harborvaleassurance.com</div>
    <div class="contact-line">harborvaleassurance.com</div>
    <div class="contact-follow">follow us: <span class="social-dot"></span><span class="social-dot"></span></div>
  </footer>
</main>
</body>
</html>
```